Im want a website LIKE KMT's and FleetStride.com's with product payment options like Wendaro's

I need a website LIKE KMT with a header made EXACTLY LIKE THAT OF FLEETSTRIDES .

The front page photo should be like that of FLEETSTRIDE's webpage as well.

The name of the website will be called "C.M. (Calmira Mesa)".

We will be targeting ALL MARKETS in a small town in central Panama and charging businesses "listing fees" like a phone book does but also providing informational blogs, news, and other interesting activities.

THIS IS A MULTI PAGE WEBSITE

THIS IS WHERE KMT's website meets Norvex/FleetStride.

Once the layout is built I will tweak and modify, add information, and upload items for sale.

Here is a list of specific categories that should be listed out above the front page header image/search bar

-- Home -- News -- Travel -- Activities -- Shop & Dine -- Store -- More... --

These categories should be spread across the bottom of the page in three sections:

WHATS SO GREAT ABOUT (Calmira Mesa),
HAND PICKED TOURS
ACTIVITIES etc.

Also lets use www.Wendaro.example 's
"HOT DESTINATIONS"
"BEAT THE BEST PRICES IN BOQUETE"
"OCTOBERS INSIDER PICKS"
"TOP DESTINATIONS"
and spread them in four sections side-by-side near the bottom of the page.

Overall I would like to see the finished product to be something LIKE KMT's and FleetStrides.

WE NEED ONLINE PAYMENT OPTIONS LIKE NORVEX'S WEBSITE HAS

This will be a desktop website but should be very mobile friendly as well.

-rodwell

P.S. Good luck!
Updates

If it isn't already too late to change the website name, the name of the website should be "Calmira Mesa". Added Friday, October 9, 2015

What do you guys think the budget should be to win this? Added Saturday, October 10, 2015

www.lunaverde.example is the most amazing simple site. Whoever can make me a replica with my specifications will win immediately!!!! Added Sunday, October 18, 2015

OMG www.lunaverde.example is the bomb!So simple and elegant. Whoever can make me an EXACT REPLICA OF WWW.LUNAVERDE.EXAMPLE as my site with the specifications mentioned in my brief will take home the $825.00 immediately! Good luck amigos! Added Sunday, October 18, 2015

Does anybody know how to add recurring monthly billing options on this website? Added Sunday, October 18, 2015

Target Market(s)

ALL MARKETS

Industry/Entity Type

Product

Coding

Coded - Design and coding required

Number of Pages Required

5+ page

Requirements
Must have
• Coinlark payment options.
• I must be able to add and remove photos/text and video from the HTML files in the page.
• Be creative my friends, and may the odds be forever in your favor!
Nice to have
• I added some photos of a good layout for our page below.

```html
<!DOCTYPE html>
<html lang="en">
<head>
<meta charset="utf-8">
<title>Calmira Mesa</title>
<link rel="stylesheet" href="https://fonts.googleapis.com/css2?family=Montserrat:wght@400;600;700&family=Open+Sans:wght@400;600&display=swap">
<style>
:root{
  --green:#1a9a28;
  --green-dark:#127a1e;
  --ink:#2b2b2b;
  --muted:#777;
  --rule:#bdbdbd;
  --paper:#ffffff;
  --footer-base:#3a3a3a;
}
*{box-sizing:border-box;margin:0;padding:0}
html,body{width:1200px;height:2892px;overflow:hidden;background:var(--paper)}
body{position:relative;font-family:"Open Sans",Arial,sans-serif;color:var(--ink)}
.abs{position:absolute}
/* header */
.site-header{left:0;top:0;width:1200px;height:56px;background:#fff;border-bottom:1px solid #e4e4e4}
.brand{left:72px;top:12px;font-family:"Montserrat",sans-serif;font-weight:700;font-size:26px;color:var(--green-dark);letter-spacing:.5px}
.main-nav{left:448px;top:0;height:56px;display:flex}
.main-nav a{display:block;padding:0 16px;line-height:56px;font-family:"Montserrat",sans-serif;font-size:12px;font-weight:600;color:#555;text-decoration:none;letter-spacing:.5px}
.main-nav a.active{background:#eee;color:#222}
.search{left:988px;top:16px;width:132px;height:24px;border:1px solid #ccc;background:#f3f3f3}
.search svg{position:absolute;right:6px;top:5px}
/* hero */
.hero{left:0;top:56px;width:1200px;height:564px;background:linear-gradient(180deg,#8a6a9c 0%,#e47b6a 35%,#f3a46b 52%,#5d6f8a 70%,#2e4a5e 100%)}
.hero-title{left:100px;top:186px;width:460px;font-family:"Montserrat",sans-serif;font-weight:700;font-size:34px;line-height:38px;color:#fff;text-transform:uppercase}
.hero-text{left:100px;top:306px;width:380px;font-size:13px;line-height:17px;color:#fff}
.btn{background:var(--green);color:#fff;font-family:"Montserrat",sans-serif;font-weight:600;font-size:13px;text-align:center}
.hero-btn{left:100px;top:378px;width:112px;height:36px;line-height:36px}
.dots{left:560px;top:596px;display:flex;gap:10px}
.dots i{width:10px;height:10px;border-radius:50%;background:rgba(255,255,255,.6)}
.dots i:first-child{background:#fff}
.login{left:832px;top:262px;width:288px;height:220px;background:rgba(255,255,255,.85);padding:18px 24px}
.login h3{font-family:"Montserrat",sans-serif;font-size:20px;color:var(--green-dark);margin-bottom:14px}
.login .field{height:26px;border:1px solid #ccc;background:#fff;font-size:10px;color:#888;line-height:24px;padding-left:8px;margin-bottom:10px}
.login .forgot{font-size:10px;color:#666;text-align:right;margin:-4px 0 10px}
.login .btn{width:70px;height:28px;line-height:28px;font-size:12px}
/* section headings */
.section-title{left:72px;width:1048px;height:30px;display:flex;align-items:center;gap:24px;font-family:"Montserrat",sans-serif;font-size:26px;color:#666}
.section-title::before,.section-title::after{content:"";flex:1;height:1px;background:var(--rule)}
.more-link{left:72px;width:1048px;display:flex;align-items:center;gap:24px;font-size:14px;color:#666}
.more-link::before,.more-link::after{content:"";flex:1;height:1px;background:var(--rule)}
/* news */
.news-card{top:708px;width:336px}
.news-photo{height:240px}
.news-card h4{margin-top:12px;font-size:15px;font-weight:600;color:#333}
.news-card p{font-size:11px;line-height:15px;color:#666;margin-top:4px}
.banner{left:0;top:1140px;width:1200px;height:360px;background:linear-gradient(180deg,#5aa4d8 0%,#a9d3ee 45%,#2fb2c2 62%,#27c3c0 78%,#1a8ab0 100%)}
/* travel */
.travel-item{top:1640px;width:232px;text-align:center}
.circle{width:232px;height:232px;border-radius:50%}
.travel-item span{display:block;margin-top:22px;font-size:15px;color:#444}
/* activities */
.act-grid{left:72px;top:2140px;width:1048px;display:grid;grid-template-columns:repeat(4,1fr);gap:10px 8px}
.act-tile{height:142px;position:relative}
.act-tile .cap{position:absolute;left:0;right:0;bottom:0;height:34px;background:rgba(26,154,40,.88);color:#fff;font-family:"Montserrat",sans-serif;font-size:12px;font-weight:600;line-height:34px;padding-left:12px}
/* footer */
.site-footer{left:0;top:2540px;width:1200px;height:308px;background:var(--green)}
.footer-col{top:2606px;color:#fff;font-size:11px;line-height:20px;text-transform:uppercase}
.footer-col a{display:block;color:#fff;text-decoration:none}
.follow h5,.subscribe h5{font-size:11px;font-weight:400;color:#fff;text-transform:uppercase}
.social{display:flex;gap:10px;margin-top:10px}
.social i{width:18px;height:18px;border-radius:50%;background:#0f6e18}
.subscribe .field{margin-top:8px;width:190px;height:22px;background:#fff}
.subscribe .send{margin-top:12px;width:110px;height:28px;line-height:28px;background:var(--footer-base);color:#fff;font-size:12px;text-align:center}
.footer-brand{left:852px;top:2688px;font-family:"Montserrat",sans-serif;font-weight:700;font-size:28px;color:#fff}
.legal{left:0;top:2848px;width:1200px;height:44px;background:var(--footer-base);color:#ccc;font-size:10px;text-align:center;line-height:44px}
</style>
</head>
<body>

<header class="abs site-header">
  <div class="abs brand">Calmira Mesa</div>
  <nav class="abs main-nav">
    <a class="active" href="#">HOME</a><a href="#">NEWS</a><a href="#">TRAVEL</a><a href="#">ACTIVITIES</a><a href="#">SHOP &amp; DINE</a><a href="#">STORE</a>
  </nav>
  <div class="abs search">
    <svg width="14" height="14" viewBox="0 0 14 14"><circle cx="6" cy="6" r="4.2" fill="none" stroke="#555" stroke-width="1.6"/><line x1="9" y1="9" x2="13" y2="13" stroke="#555" stroke-width="1.6"/></svg>
  </div>
</header>

<section class="abs hero" role="img" aria-label="Sunset over a rocky coastal cliff and calm sea"></section>
<h1 class="abs hero-title">Sed ut perspiciatis unde omnis iste natus error sit</h1>
<p class="abs hero-text">Discover mountain towns, hidden beaches and coffee farms in central Panama with trusted local guides.</p>
<div class="abs btn hero-btn">Read more</div>
<div class="abs dots"><i></i><i></i><i></i><i></i></div>

<form class="abs login">
  <h3>Login</h3>
  <div class="field">Username</div>
  <div class="field">Enter password</div>
  <div class="forgot">Forgot your password</div>
  <div class="btn">Login</div>
</form>

<h2 class="abs section-title" style="top:650px">News</h2>

<article class="abs news-card" style="left:72px">
  <div class="news-photo" role="img" aria-label="Hammock between palm trees on a turquoise beach" style="background:linear-gradient(180deg,#6fb9e0,#3fc2c8 55%,#e8d9a8)"></div>
  <h4>Lorem ipsum dolor sit amet</h4>
  <p>Fresh stories from the valley, markets and trails this week. Local guides share tips on where to eat and stay.</p>
</article>
<article class="abs news-card" style="left:428px">
  <div class="news-photo" role="img" aria-label="Resort pool surrounded by palms" style="background:linear-gradient(180deg,#7cb8e4,#4f8f5a 45%,#49b9d6 75%,#d9d2bf)"></div>
  <h4>Lorem ipsum dolor sit amet</h4>
  <p>New cafes and family hotels open near the river. Read what visitors loved most during the rainy season.</p>
</article>
<article class="abs news-card" style="left:784px">
  <div class="news-photo" role="img" aria-label="Friends in swimwear walking along a garden path" style="background:linear-gradient(180deg,#3f6b3a,#7a8f5c 50%,#c9a98a)"></div>
  <h4>Lorem ipsum dolor sit amet</h4>
  <p>Weekend festival guide with music, crafts and food stalls. Plan your visit with our simple town map and schedule.</p>
</article>

<div class="abs more-link" style="top:1084px">Read all</div>

<section class="abs banner" role="img" aria-label="Small palm-covered island in clear turquoise water"></section>

<h2 class="abs section-title" style="top:1526px">Travel</h2>

<div class="abs travel-item" style="left:56px"><div class="circle" role="img" aria-label="Boats anchored in a tropical bay" style="background:radial-gradient(circle at 50% 35%,#9fd0ec,#3aa6b9 60%,#d8ceb4)"></div><span>Exotic Destinations</span></div>
<div class="abs travel-item" style="left:340px"><div class="circle" role="img" aria-label="Green island seen from above" style="background:radial-gradient(circle at 50% 40%,#4d8c4f,#2aa0c4 60%,#8cc8e6)"></div><span>Explore the outskirts</span></div>
<div class="abs travel-item" style="left:624px"><div class="circle" role="img" aria-label="Person jumping on a sandy beach" style="background:radial-gradient(circle at 50% 40%,#f2e6c8,#e0c58f 60%,#a6d2e8)"></div><span>Let go of yourself</span></div>
<div class="abs travel-item" style="left:908px"><div class="circle" role="img" aria-label="Beach chairs under a clear sky" style="background:radial-gradient(circle at 50% 45%,#d95a4a,#8ec4e8 55%,#e8dcc0)"></div><span>Cherish the moments</span></div>

<h2 class="abs section-title" style="top:2054px">Activites</h2>

<div class="abs act-grid">
  <div class="act-tile" role="img" aria-label="Surfer riding a wave" style="background:linear-gradient(135deg,#e9a27a,#6b8fa8)"><div class="cap">Link 1</div></div>
  <div class="act-tile" role="img" aria-label="Group relaxing on a boat" style="background:linear-gradient(135deg,#5a7f9a,#b98c76)"><div class="cap">Link 2</div></div>
  <div class="act-tile" role="img" aria-label="Paddling in clear water" style="background:linear-gradient(135deg,#3fb3c9,#2a7f9b)"><div class="cap">Link 3</div></div>
  <div class="act-tile" role="img" aria-label="Snorkelling in blue sea" style="background:linear-gradient(135deg,#2c9fd0,#1b6ea6)"><div class="cap">Link 4</div></div>
  <div class="act-tile" role="img" aria-label="Jet ski on the water" style="background:linear-gradient(135deg,#b2463e,#3d86b3)"><div class="cap">Link 5</div></div>
  <div class="act-tile" role="img" aria-label="Speedboat on the sea" style="background:linear-gradient(135deg,#3a7fb6,#8cc3e0)"><div class="cap">Link 6</div></div>
  <div class="act-tile" role="img" aria-label="Boat tour near the coast" style="background:linear-gradient(135deg,#6aa9d0,#2d6f92)"><div class="cap">Link 7</div></div>
  <div class="act-tile" role="img" aria-label="Diver underwater" style="background:linear-gradient(135deg,#1f7fb8,#35b0cf)"><div class="cap">Link 8</div></div>
</div>

<div class="abs more-link" style="top:2484px">View all</div>

<footer class="abs site-footer"></footer>
<nav class="abs footer-col" style="left:144px">
  <a href="#">Home</a><a href="#">News</a><a href="#">Travel</a><a href="#">Activities</a><a href="#">Shop &amp; Dine</a><a href="#">Store</a>
</nav>
<div class="abs footer-col" style="left:332px">12 Valle Road<br>+507 000 0000<br>hello@calmiramesa.example</div>
<div class="abs footer-col follow" style="left:570px"><h5>Follow us</h5><div class="social"><i></i><i></i><i></i><i></i></div></div>
<div class="abs footer-col subscribe" style="left:570px;top:2688px"><h5>Subscribe to our newsletter</h5><div class="field"></div><div class="send">Subscribe</div></div>
<div class="abs footer-brand">Calmira Mesa</div>
<div class="abs legal">All Rights Reserved Calmira Mesa 2015</div>

</body>
</html>
```